A5 Patient Information Booklet (Chiropractic Clinic) 4-8 pages

Here’s a polished, professional rewrite of your full brief and content, with clearer structure, corrected language, and a premium tone:

---

**Project Title:** Premium Patient Information Brochure (Chiropractic & Wellness Clinic)

---

### **Overview**

We are a health and wellness clinic seeking a premium, high-end patient information brochure to provide following a patient’s initial consultation and first treatment.

The purpose of this booklet is to:

* Reinforce trust and professionalism
* Help patients understand what to expect next
* Encourage adherence to care recommendations
* Position the clinic as calm, expert-led, and results-driven

---

### **Format**

* 4–8 page booklet (A5 or similar size)
* Print-ready and digital versions required

---

### **Target Audience**

Patients who have just completed their initial consultation and may have begun treatment. They may already be experiencing physical or mental changes, so the brochure should guide, reassure, and educate them on what comes next.

---

### **Tone & Style**

* Premium, calm, and reassuring
* Modern wellness aesthetic (not overly clinical)
* Clean layout with minimal clutter
* Soft, neutral colour palette (whites, creams, muted greens, soft blues)
* Elegant typography (e.g. Montserrat / Lato)
* High-end, trustworthy, and professional feel

---

### **Key Messages**

#### 1. Listen to Your Body

Patients may feel different after treatment. Reassure them that this is normal and part of the healing process.

#### 2. Post-Treatment Advice

* Stay well hydrated
* Rest if needed
* Avoid overexertion if the body requires recovery

#### 3. Healing is a Journey (Core Concept)

A strong visual metaphor of a **“road to recovery”** or **journey** should be central to the design.

This journey should clearly illustrate three phases:

* **Phase 1: Initial Care (Weeks 1–6)**
Focus: Reducing pain/discomfort, calming the body, and initiating response to treatment

* **Phase 2: Corrective Care (Weeks 6–12)**
Focus: Addressing underlying issues, improving function, and creating lasting change

* **Phase 3: Wellness / Maintenance (Ongoing)**
Focus: Maintaining progress, preventing relapse, and supporting long-term wellbeing

**Important:**

* Emphasise that this is not a quick fix
* Progress requires time and consistency
* Each patient follows an individualised care plan
* The journey should feel structured, positive, and achievable

#### 4. Personalised Care

Reinforce that every treatment plan is tailored specifically to the individual.

#### 5. Professional Reassurance

Patients should feel confident they are in expert hands and supported throughout their journey.

---

### **Design Direction**

* Use imagery that reflects calmness, progression, and wellness (e.g. pathways, nature, soft gradients)
* Avoid generic stock imagery
* **Only use original clinic images from website and social media**
* Prioritise white space and clarity
* Aim for a luxury spa/medical hybrid aesthetic

---

## **Content Structure (Page-by-Page)**

### **Front Cover**

* Clean, minimal, premium design
* Clinic branding

---

### **Page 1: Patient Case Summary**

**Title:** *Welcome to Fernwell Practice*

Thank you for choosing Fernwell Practice.

This booklet is designed to guide you through:

* What we found during your initial consultation
* Your personalised recommended treatment plan
* Your road to recovery
* Long-term wellness care
* Why we take the approach we do

---

### **Page 2: Your Care Journey**

**Stage 1: Your Initial Consultation**

Today we completed a comprehensive assessment of your health and function, including:

* Full case history and discussion of your symptoms and goals
* Orthopaedic and neurological testing
* Postural and movement assessment
* Initial treatment (where appropriate)

**What this tells us:**

* How your body is currently functioning
* Where areas of stress or dysfunction may be present
* The most appropriate and effective path forward for your care

---

### **Page 3: Your Suggested Treatment Plan**

Based on today’s findings, your recommended care plan is:

**______ treatments over ______ weeks**

This should be viewed alongside your *Road to Recovery* to help you understand what to expect.

We have also discussed:

* Expected timelines for improvement
* Available payment options

**After Treatment:**
It is common to feel different following treatment. This is a normal response as your body begins to adapt and respond.

We recommend:

* Staying well hydrated
* Allowing time for rest and recovery
* Avoiding overexertion if your body feels it needs it

---

### **Page 4: What to Expect Next**

Healing is not always linear—it is a process that occurs over time.

Your care will typically progress through the following stages:

* **Relief Care**
Focused on reducing discomfort and calming the body

* **Corrective Care**
Focused on addressing underlying issues and improving function
(This phase may include prescribed exercises)

* **Maintenance / Wellness Care**
Focused on sustaining progress, preventing recurrence, and supporting long-term health

---

### **Page 5: Understanding Chiropractic Care**

**What is Chiropractic?**
Chiropractic care focuses on the relationship between the spine, nervous system, and overall body function.

By improving spinal movement and alignment, chiropractic care helps support the nervous system, allowing the body to function and heal more effectively.

**About Fernwell Practice**
At Fernwell Practice, our approach is centred around personalised, patient-focused care. We aim to not only relieve symptoms but to address underlying causes and support long-term wellbeing.

---

### **Back Page**

* Clinic contact details
* Website
* Social media icons/handles

**Closing Message:**
“A healthier, stronger you—supported every step of the way.”

---

### **Deliverables**

* Print-ready PDF
* Editable source files

---

### **Additional Notes**

* The brochure should feel valuable and worth keeping
* Encourage long-term care in a subtle, non-pushy way
* Maintain clarity, readability, and strong visual hierarchy
* Balance professionalism with warmth and approachability

---

If you’d like, I can also turn this into **actual brochure copy (fully written, patient-facing text)** or help you refine it further for a designer.

Target Market(s)

Existing patients who want to feel better and look after themselves that is given after their initil consultation appointment

Industry/Entity Type

Chiropractic, wellness, health

Font styles to use
Other font styles liked:
• Montserrat or Lato

Colors
0094D4
00A9DD
6FCCEA
C7EBF8
E9F6FB
00AB8E
00BBA5
67D7C9
C6EFE9
E9F9F6
6B429C
8869AF
B7A5CE
E3DAEB
F3F0F8

Requirements
Must have
• my own photos, look premium wellness, be clear and simple to understand for patients journey or what to expect next and over time
Nice to have
• USe my social media/website for ideas
Should not have
• generic photos and images

```html
<!DOCTYPE html>
<html lang="en">
<head>
<meta charset="utf-8">
<title>Fernwell Practice – Patient Information Booklet</title>
<link href="https://fonts.googleapis.com/css2?family=Montserrat:ital,wght@0,400;0,500;0,600;0,700;0,800;1,600;1,700&display=swap" rel="stylesheet">
<style>
:root{
  --backdrop:#6e6e6e;
  --teal:#00aba1;
  --teal-deep:#0f9c92;
  --pink:#f77fc0;
  --violet:#a68fd6;
  --sky:#6ab3e6;
  --ink:#2a1f1f;
  --text:#3a3a3a;
  --white:#ffffff;
  --map:#eef8f7;
}
*{box-sizing:border-box;margin:0;padding:0}
html,body{width:1200px;height:2361px;overflow:hidden}
body{background:var(--backdrop);font-family:'Montserrat',sans-serif;color:var(--text);position:relative}

/* ---------- outer spread ---------- */
.spread{position:absolute;left:100px;top:80px;width:1000px;height:707px;background:var(--white);overflow:hidden;box-shadow:0 14px 30px rgba(0,0,0,.35)}
.spread-shapes{position:absolute;inset:0}
.why{position:absolute;left:38px;top:40px;width:470px;color:var(--white)}
.why h2{font-weight:800;font-size:19px;letter-spacing:.3px}
.why .lead{font-style:italic;font-weight:700;font-size:12.5px;margin:4px 0 6px}
.why ul{list-style:none}
.why li{font-size:11.5px;font-weight:600;line-height:1.45;padding-left:16px;position:relative}
.why li::before{content:"";position:absolute;left:2px;top:5px;width:8px;height:8px;border-radius:50%;background:var(--white)}
.why .bio{font-size:11.5px;font-weight:600;line-height:1.45;margin-top:10px;width:400px}
.book{position:absolute;left:40px;top:392px;width:200px}
.book h3{color:var(--teal);font-weight:800;font-size:13px}
.book p{font-weight:700;font-size:12px;line-height:1.3;color:var(--ink)}
.contact{position:absolute;left:40px;top:478px;width:215px;font-size:10.5px;color:var(--ink)}
.contact .socials{display:flex;gap:4px;margin-bottom:6px}
.contact .socials span{width:12px;height:12px;border-radius:2px;background:var(--teal)}
.contact .name{font-weight:800;font-size:12.5px}
.contact .sub{color:var(--teal);font-weight:700;font-size:11px;margin-bottom:4px}
.contact .row{display:flex;align-items:center;gap:6px;line-height:1.55}
.contact .row i{width:8px;height:8px;border-radius:50%;background:var(--teal);flex:none}
.brand-mark{display:flex;flex-direction:column;align-items:center;gap:6px;font-family:'Montserrat',sans-serif;font-weight:800;color:var(--ink);letter-spacing:.5px;text-transform:uppercase;text-align:center;line-height:1.1}
.brand-mark i{display:block;border-radius:50%;border:3px solid var(--teal);flex:none}
.back-brand{position:absolute;left:262px;top:430px;width:200px;font-size:15px}
.back-brand i{width:30px;height:30px}
.map{position:absolute;left:262px;top:520px;width:200px;height:122px;border:2px solid var(--teal);border-radius:10px;background:var(--map)}
.photo{position:absolute;border-radius:50%}
.photo-main{left:545px;top:50px;width:330px;height:330px;background:radial-gradient(circle at 45% 40%,#e9e2dc,#a59585 55%,#5a4a40);border:8px solid var(--white)}
.photo-bw{left:478px;top:355px;width:175px;height:175px;background:radial-gradient(circle at 50% 45%,#d8d8d8,#8a8a8a 60%,#3a3a3a);border:6px solid var(--white)}
.logo-disc{position:absolute;left:770px;top:60px;width:220px;height:220px;border-radius:50%;background:var(--white);display:flex;align-items:center;justify-content:center}
.logo-disc .brand-mark{font-size:17px;width:180px}
.logo-disc .brand-mark i{width:36px;height:36px}
.cover-copy{position:absolute;right:40px;top:525px;width:370px;text-align:right;color:var(--ink)}
.cover-copy h1{font-weight:800;font-size:20px;line-height:1.1}
.cover-copy p{font-weight:600;font-size:11.5px;line-height:1.35;margin-top:8px}
.cover-copy .url{display:inline-block;margin-top:10px;background:var(--ink);color:var(--white);font-weight:700;font-size:12px;padding:6px 18px;border-radius:16px}

/* ---------- inner pages ---------- */
.page{position:absolute;width:458px;height:649px;background:linear-gradient(180deg,var(--pink) 0%,var(--violet) 50%,var(--sky) 100%)}
.page-card{position:absolute;inset:26px;background:var(--white);border-radius:8px;padding:22px 24px;overflow:hidden}
.p1{left:118px;top:938px}.p2{left:625px;top:938px}.p3{left:118px;top:1637px}.p4{left:625px;top:1637px}
.title{color:var(--teal);font-weight:800;letter-spacing:.2px}
.body{font-size:8.6px;line-height:1.22;text-align:justify}
.body b{font-weight:700}
.ticks{list-style:none}
.ticks li{position:relative;padding-left:12px;font-size:8.6px;line-height:1.22;margin-bottom:7px}
.ticks li::before{content:"";position:absolute;left:0;top:2px;width:7px;height:7px;border-radius:50%;background:var(--teal)}
.ticks li::after{content:"";position:absolute;left:2px;top:3px;width:2px;height:3px;border:solid var(--white);border-width:0 1.2px 1.2px 0;transform:rotate(40deg)}
.pic{position:absolute;background:linear-gradient(160deg,#f1ece6,#c7b8aa 55%,#7c8fa8)}

/* page 1 */
.p1 .title{font-size:20px;margin-bottom:6px}
.p1 .portrait{position:absolute;left:24px;top:118px;width:110px;height:110px;border-radius:50%;background:radial-gradient(circle at 50% 40%,#efe6dd,#b59a84 60%,#6b8cae)}
.p1 .intro{position:absolute;left:142px;top:122px;width:240px}
.p1 .about{position:absolute;left:24px;top:232px;width:358px}
.p1 .after{position:absolute;left:24px;top:322px;width:170px}
.p1 .after .lead{font-size:8.6px;font-weight:700;color:var(--ink);line-height:1.22;margin-bottom:8px;text-align:justify}
.p1 .after .trust{font-size:8.6px;line-height:1.22;margin-top:4px}
.p1 .pic{left:218px;top:318px;width:164px;height:256px}

/* page 2 */
.p2 .title{font-size:15px}
.p2 .sub{font-weight:700;font-size:11px;color:var(--ink);line-height:1.2;margin:3px 0 8px}
.p2 .list-top{width:360px}
.p2 .list-narrow{width:190px}
.p2 .callout{font-size:9.5px;font-weight:600;color:var(--ink);line-height:1.2;width:190px;margin:6px 0 22px}
.p2 .q{font-size:15px;line-height:1.2}
.p2 .q-sub{font-weight:600;font-size:12px;color:var(--ink);line-height:1.2;margin:4px 0 8px}
.p2 .right-list li{font-size:9.5px}
.p2 .pic{left:220px;top:136px;width:162px;height:366px}
.p2 .foot{position:absolute;left:24px;top:514px;width:360px}
.p2 .foot .body{font-size:9px;margin-bottom:8px}
.p2 .foot .cond{font-size:9px;font-weight:700;color:var(--ink)}

/* page 3 */
.p3 .title{color:var(--ink);font-size:17px}
.p3 .col{position:absolute;left:24px;top:46px;width:170px}
.p3 h4{font-size:11px;font-weight:600;color:var(--teal);text-decoration:underline;display:flex;align-items:center;gap:5px;margin-bottom:3px}
.p3 h4 .num{background:var(--ink);color:var(--white);font-size:9px;width:11px;height:11px;display:inline-flex;align-items:center;justify-content:center;text-decoration:none}
.p3 .blk{margin-bottom:14px}
.p3 .phase{font-size:9px;line-height:1.2;margin-bottom:10px}
.p3 .phase b{color:var(--teal)}
.p3 .phase strong{color:var(--ink)}
.p3 .ticks li{margin-bottom:3px}
.p3 .pic{left:214px;top:20px;width:170px;height:415px}
.p3 .important{position:absolute;left:24px;top:446px;width:170px}
.p3 .important h5{color:var(--teal);font-size:11px;font-weight:800;text-decoration:underline;margin-bottom:4px}
.p3 .important .ticks li{margin-bottom:6px}
.p3 .extras{position:absolute;left:214px;top:446px;width:170px}
.p3 .extras h4{text-decoration:none;font-size:11px}

/* page 4 */
.p4 .title{font-size:18px;text-align:center;text-decoration:underline;margin-top:14px}
.p4 .field{font-weight:600;font-size:14px;color:var(--ink);margin-top:40px}
.p4 .line{border-bottom:1px solid var(--ink);height:26px}
.p4 .blank-row{font-size:14px;color:var(--ink);display:flex;align-items:flex-end;gap:6px;margin-top:20px}
.p4 .blank-row span{border-bottom:1px solid var(--ink);display:inline-block;height:14px}
.p4 .chart-frame{position:absolute;left:32px;top:324px;width:344px;height:244px;border:6px solid #333;background:var(--white)}
.p4 .chart{position:absolute;inset:0;background:linear-gradient(90deg,#e9f6fb 0%,#fdeed7 40%,#e6f4d8 70%,#dfeefa 100%)}
</style>
</head>
<body>

<section class="spread" aria-label="Brochure outer spread">
  <svg class="spread-shapes" viewBox="0 0 1000 707" width="1000" height="707" aria-hidden="true">
    <defs>
      <linearGradient id="coverBand" x1="1" y1="0" x2="0" y2="1">
        <stop offset="0" stop-color="#f77fc0"/>
        <stop offset="0.55" stop-color="#b08cd6"/>
        <stop offset="1" stop-color="#7aa7e0"/>
      </linearGradient>
    </defs>
    <path d="M0 0 H690 V160 C600 330 460 370 300 360 C180 352 80 330 0 300 Z" fill="#00aba1"/>
    <path d="M360 707 C400 610 500 540 620 515 C770 485 900 430 1000 300 V707 Z" fill="url(#coverBand)"/>
  </svg>

  <div class="why">
    <h2>WHY CHOOSE FERNWELL PRACTICE?</h2>
    <p class="lead">Patients choose Fernwell Practice because we offer:</p>
    <ul>
      <li>Personalised care — never rushed, never one-size-fits-all</li>
      <li>Clear explanations — no jargon, no pressure</li>
      <li>A calm, welcoming environment</li>
      <li>Care for adults and families</li>
      <li>A wellness-focused approach, not just symptom chasing</li>
      <li>Easy online booking and access to our very own app</li>
      <li>We aim to support your health now and help you stay well into the future</li>
    </ul>
    <p class="bio">Clara, a first-class honours graduate and chiropractic lecturer, brings expert care with a gentle, personalised approach that helps every patient feel heard and supported.</p>
  </div>

  <div class="book">
    <h3>BOOK AN APPOINTMENT</h3>
    <p>Booking your appointment at Fernwell Practice is simple and convenient.</p>
  </div>

  <div class="contact">
    <div class="socials"><span></span><span></span></div>
    <div class="name">FERNWELL PRACTICE</div>
    <div class="sub">Chiropractic &amp; Wellness</div>
    <div class="row"><i></i>12 Mill Lane, Ashbury AB1 2CD</div>
    <div class="row"><i></i>info@fernwellpractice.com</div>
    <div class="row"><i></i>www.fernwellpractice.com</div>
  </div>

  <div class="brand-mark back-brand"><i></i>Fernwell Practice</div>
  <div class="map" role="img" aria-label="Street map showing the clinic location"></div>

  <div class="photo photo-main" role="img" aria-label="Chiropractor treating a patient on a treatment table"></div>
  <div class="photo photo-bw" role="img" aria-label="Black and white photo of a chiropractor adjusting a patient's neck"></div>
  <div class="logo-disc"><div class="brand-mark"><i></i>Fernwell Practice</div></div>

  <div class="cover-copy">
    <h1>ALIGN YOUR BODY,<br>ELEVATE YOUR WELLBEING</h1>
    <p>At Fernwell Practice Chiropractic and Wellness Ashbury, we offer personalised chiropractic care for adults &amp; families who want to feel their best — whether that's easing discomfort, improving movement, or supporting long-term wellbeing.</p>
    <span class="url">www.fernwellpractice.com</span>
  </div>
</section>

<section class="page p1">
  <div class="page-card">
    <h2 class="title">WHAT IS CHIROPRACTIC CARE?</h2>
    <p class="body">Chiropractic care focuses on how your body moves, functions, and heals as a whole. By improving the alignment and mobility of the spine and joints, we help reduce pressure on the nervous system, allowing your body to function more efficiently. Rather than simply masking symptoms, our approach supports your body's natural ability to adapt, recover, and maintain long-term health.</p>
    <div class="portrait" role="img" aria-label="Portrait of the clinic chiropractor"></div>
    <p class="body intro">Your Chiropractor At Fernwell Practice, your care is led by <b>chiropractor Clara</b>, who takes a personalised, hands-on approach to your health. Every consultation is focused on understanding your body, your lifestyle, and your goals—so your treatment plan is tailored specifically to you. Clara combines clinical expertise with a calm, supportive environment to help you feel confident, informed, and in control of your recovery journey.</p>
    <p class="body about">About Fernwell Practice At Fernwell Practice, we believe that true health is built over time—not achieved through quick fixes. Our approach is centred around personalised care, attention to detail, and long-term results. We work with you to not only relieve symptoms, but to improve how your body functions and performs in everyday life. Every step of your journey is guided with care, clarity, and a focus on lasting wellbeing.</p>
    <div class="after">
      <p class="lead">What to Expect After Your Treatment It's completely normal to feel different after your treatment. As your body begins to respond and adapt, you may notice changes in movement, tension, or overall wellbeing.</p>
      <ul class="ticks">
        <li>Stay Hydrated Drinking plenty of water supports your body's natural recovery process.</li>
        <li>Listen to Your Body You may feel relief, mild soreness, or changes in how your body moves—these are all normal signs of adjustment.</li>
        <li>Rest When Needed Give your body time to recover. Avoid overexertion if your body feels like it needs rest.</li>
      </ul>
      <p class="trust">Trust the Process Meaningful, lasting change takes time. Each step of your care plan is designed to support long-term results—not just short-term relief.</p>
    </div>
    <div class="pic" role="img" aria-label="Chiropractor treating a patient lying on a treatment table"></div>
  </div>
</section>

<section class="page p2">
  <div class="page-card">
    <h2 class="title">WHAT TO EXPECT AT YOUR FIRST VISIT</h2>
    <p class="sub">Your first appointment is relaxed, thorough and focused on understanding you.</p>
    <ul class="ticks list-top">
      <li>We'll talk about your health, concerns, and goals</li>
      <li>You'll have a detailed assessment of your posture and how your body moves, including orthopaedic and neurological testing to identify the root cause of your symptoms</li>
    </ul>
    <ul class="ticks list-narrow">
      <li>We'll explain what we find in clear, simple terms</li>
      <li>Care is tailored specifically to you</li>
      <li>If appropriate, we'll outline a plan that makes sense for your lifestyle</li>
      <li>There's no pressure — just clear guidance and supportive care.</li>
    </ul>
    <p class="callout">If you're looking for a chiropractor in Ashbury, we'd love to help.</p>
    <h3 class="title q">Is Chiropractic right<br>for me?</h3>
    <p class="q-sub">Chiropractic care can help<br>if you:</p>
    <ul class="ticks list-narrow right-list">
      <li>Feel uncomfortable, stiff, or restricted</li>
      <li>Experience recurring aches or tension</li>
      <li>Want to support your body's movement and function</li>
      <li>Are interested in proactive, wellness-based care</li>
      <li>Have tried other options without lasting results</li>
    </ul>
    <div class="pic" role="img" aria-label="Chiropractor assessing a seated patient's back"></div>
    <div class="foot">
      <p class="body">You don't need a referral &amp; you don't need to be "broken" to benefit. Many people choose chiropractic care to stay well, not just to get out of pain.</p>
      <p class="cond">Conditions treated: Back pain, Sciatica, Neck pain, Headaches, Sports injuries and many more!</p>
    </div>
  </div>
</section>

<section class="page p3">
  <div class="page-card">
    <h2 class="title">KEY MESSAGES:</h2>
    <div class="col">
      <div class="blk">
        <h4><span class="num">1</span>Listen to Your Body</h4>
        <p class="body">Patients may feel different after treatment. Encourage awareness and reassurance that this is normal.</p>
      </div>
      <div class="blk">
        <h4><span class="num">2</span>Post-Treatment Advice</h4>
        <ul class="ticks">
          <li>Stay well hydrated</li>
          <li>Rest if needed</li>
          <li>Avoid overexertion if the body feels like it needs recovery</li>
        </ul>
      </div>
      <div class="blk">
        <h4><span class="num">3</span>Healing is a Journey</h4>
        <p class="phase"><b>Phase 1:</b> <strong>Initial Care (Weeks 1–6)</strong><br><b>FOCUS:</b> Reducing pain/discomfort, calming the body and helping you begin to respond to treatment.</p>
        <p class="phase"><b>Phase 2:</b> <strong>Corrective Care<br>(Weeks 6–12)</strong><br><b>FOCUS:</b> Addressing underlying issues, improving function, and creating more stable, lasting changes.</p>
        <p class="phase"><b>Phase 3:</b> <strong>Wellness /<br>Maintenance (Ongoing)</strong><br><b>FOCUS:</b> Maintaining progress, preventing relapse, and supporting long-term health and wellbeing.</p>
      </div>
    </div>
    <div class="pic" role="img" aria-label="Chiropractor adjusting a patient lying on a treatment table"></div>
    <div class="important">
      <h5>IMPORTANT:</h5>
      <ul class="ticks">
        <li>This visual should clearly communicate that this is not a quick fix</li>
        <li>Progress takes time &amp; consistency</li>
        <li>Each patient will follow an individualised treatment plan</li>
        <li>The journey should feel positive, structured, and achievable</li>
      </ul>
    </div>
    <div class="extras">
      <div class="blk">
        <h4><span class="num">4</span>Personalised Care</h4>
        <p class="body">Reinforce that each patient's treatment plan is tailored specifically to them.</p>
      </div>
      <div class="blk">
        <h4><span class="num">5</span>Professional Reassurance</h4>
        <p class="body">Patients should feel confident they are in expert hands and supported throughout their journey.</p>
      </div>
    </div>
  </div>
</section>

<section class="page p4">
  <div class="page-card">
    <h2 class="title">PERSONALISATION SECTION :</h2>
    <p class="field">* Patient Name:</p>
    <div class="line"></div>
    <p class="field">* Your Suggested Care Plan:</p>
    <p class="blank-row"><span style="width:205px"></span>treatments over</p>
    <p class="blank-row"><span style="width:155px"></span>weeks.</p>
    <div class="chart-frame">
      <div class="chart" role="img" aria-label="Road to recovery chart: a winding road rising from suffering through healing and correcting phases to optimal wellbeing over days, weeks, months and years"></div>
    </div>
  </div>
</section>

</body>
</html>
```